Helicopter Company - Skyvane Sweden

I need a new design and implementation of a webpage. We rent helicopters and are also starting a school. We havre started a wordpress but the page is very ugly. Need a complete update. Logo exist already. We also have some pictures of helicotopers. We are open for all designs but it is important that it looks professionel, is eassy to update and will give an impression och structure and dicipline.
Updates

Target Market(s)

Customers that what to get a certificate to fly. It is expensive so it’s either people with a lot of money or people with a big dream. It is very serious business.

Industry/Entity Type

www.skyvane-demo.se

Coding

Coded - Design and coding required

Number of Pages Required

4 page

Font styles to use
Sans Serif

Colors
0054AA
0677BA
7BADD7
CADEEF
E8F1F8

Requirements
Must have
• A easy page the gives a feeling of seriousness and

```html
<!DOCTYPE html>
<html lang="sv">
<head>
<meta charset="utf-8">
<title>Skyvane Sweden – Hyr helikopter</title>
<link href="https://fonts.googleapis.com/css2?family=Montserrat:wght@400;500;600;700&display=swap" rel="stylesheet">
<style>
:root{
  --blue:#0054AA;
  --blue-mid:#0677BA;
  --blue-light:#7BADD7;
  --blue-pale:#CADEEF;
  --blue-mist:#E8F1F8;
  --navy:#0B2550;
  --yellow:#F7C300;
  --text:#8A8F99;
  --white:#fff;
  --gray-bg:#F5F5F5;
}
*{margin:0;padding:0;box-sizing:border-box}
html,body{width:1200px;height:4793px;overflow:hidden}
body{font-family:"Montserrat",sans-serif;color:var(--text);background:var(--white);position:relative}
section,header,footer{position:absolute;left:0;width:1200px}
.abs{position:absolute}
.eyebrow{color:var(--yellow);font-weight:700;font-size:19px;text-transform:uppercase}
.heading{color:var(--blue);font-weight:600;line-height:1.25}
.body{font-size:13px;line-height:1.65;color:var(--text)}
.btn{position:absolute;display:flex;align-items:center;justify-content:center;font-size:11px;font-weight:600;border-radius:2px}
.btn-yellow{background:var(--yellow);color:var(--white)}
.btn-outline{border:1.5px solid var(--yellow);color:var(--yellow);background:var(--white)}
.photo{position:absolute}

/* hero */
.hero{top:0;height:558px}
.hero-bg{inset:0;background:linear-gradient(160deg,#27456f 0%,#0d2a55 45%,#13305a 70%,#0a1f40 100%)}
.brand{position:absolute;color:var(--yellow);font-weight:600;font-size:22px;letter-spacing:1px;display:flex;align-items:center;gap:8px}
.brand i{width:10px;height:10px;background:var(--yellow);border-radius:50%;display:block}
.nav{left:285px;top:24px;display:flex;gap:20px;color:var(--white);font-size:13px;font-weight:500}
.hero-title{left:0;width:1200px;top:214px;text-align:center;color:var(--white);font-size:46px;font-weight:600}
.hero-sub{left:0;width:1200px;top:280px;text-align:center;color:var(--white);font-size:28px;font-weight:500}
.social{left:1046px;width:42px;height:42px;border:3px solid var(--white);border-radius:10px}

/* services */
.card{position:absolute;top:512px;width:301px;height:227px;background:var(--white);box-shadow:0 4px 16px rgba(0,0,0,.12);text-align:center}
.card svg{margin-top:28px}
.card h3{color:var(--blue);font-weight:600;font-size:21px;margin-top:12px}
.card p{font-size:13px;line-height:1.6;margin:10px 34px 0}

/* fleet */
.stat{position:absolute;left:1010px;display:flex;gap:12px;align-items:flex-start}
.stat .dot{width:11px;height:11px;background:var(--yellow);border-radius:50%;margin-top:8px}
.stat b{color:var(--blue);font-size:20px;font-weight:600}
.stat b small{font-size:10px}
.stat span{display:block;color:var(--yellow);font-size:12px}

/* video */
.video{top:1386px;height:489px}

/* about */
.about{top:1875px;height:603px;background:var(--gray-bg)}

/* how it works */
.how-text{font-size:12px;line-height:1.75;color:var(--text)}

/* testimonials */
.quote{position:absolute;top:3892px;height:214px;background:var(--white);box-shadow:0 2px 14px rgba(0,0,0,.08);text-align:center;padding:30px 28px}
.quote p{font-size:12px;line-height:1.5}
.author{display:flex;align-items:center;justify-content:center;gap:10px;margin-top:28px;text-align:left}
.author i{width:38px;height:38px;border-radius:50%;background:linear-gradient(135deg,#7BADD7,#2d4e6e);display:block}
.author b{color:var(--yellow);font-size:13px;font-weight:500;display:block}
.author span{color:var(--blue);font-size:10px;font-weight:600}

/* partners */
.partners{top:4301px;height:146px;background:var(--gray-bg);display:flex;align-items:center;justify-content:space-around;padding:0 90px}
.partner{display:flex;align-items:center;gap:8px;color:#333;font-weight:700;font-size:25px}
.partner i{width:28px;height:28px;background:#333;display:block}

/* footer */
.footer{top:4447px;height:346px;background:linear-gradient(180deg,#0a57b0,#0050a6)}
.footer h4{position:absolute;top:74px;color:var(--white);font-size:19px;font-weight:600}
.footer p{position:absolute;color:var(--white);font-size:12.5px;line-height:1.45}
</style>
</head>
<body>

<header class="hero">
  <div class="photo hero-bg" role="img" aria-label="Utsikt från helikopterns cockpit över en storstad"></div>
  <div class="brand" style="left:112px;top:18px"><i></i>SKYVANE</div>
  <nav class="abs nav"><span>START</span><span>OM OSS</span><span>KONTAKT</span></nav>
  <div class="btn btn-yellow" style="left:992px;top:15px;width:95px;height:35px">BOKA NU</div>
  <h1 class="abs hero-title">Välkommen till Skyvane</h1>
  <p class="abs hero-sub">Hyr din helikopter av oss!</p>
  <div class="btn btn-yellow" style="left:536px;top:331px;width:128px;height:32px">Läs mer om oss</div>
  <div class="abs social" style="top:228px"></div>
  <div class="abs social" style="top:288px"></div>
</header>

<section style="top:0;height:760px;pointer-events:none">
  <div class="card" style="left:112px">
    <svg width="60" height="62" viewBox="0 0 60 62" fill="none" stroke="#F7C300" stroke-width="3"><line x1="6" y1="6" x2="54" y2="6"/><line x1="30" y1="6" x2="30" y2="16"/><rect x="20" y="16" width="20" height="22" rx="8"/><line x1="30" y1="38" x2="30" y2="52"/><line x1="14" y1="56" x2="46" y2="56"/><line x1="20" y1="38" x2="16" y2="56"/><line x1="40" y1="38" x2="44" y2="56"/></svg>
    <h3>Uthyrning</h3>
    <p>Lorem ipsum dolor sit amet, consectetur adipiscing elit, sed do eiusmod</p>
  </div>
  <div class="card" style="left:448px">
    <svg width="66" height="62" viewBox="0 0 66 62" fill="none" stroke="#F7C300" stroke-width="3"><rect x="4" y="6" width="58" height="40" rx="3"/><line x1="14" y1="18" x2="40" y2="18"/><line x1="14" y1="26" x2="40" y2="26"/><line x1="14" y1="34" x2="30" y2="34"/><circle cx="50" cy="40" r="8"/><path d="M45 47 L43 58 L50 54 L57 58 L55 47"/></svg>
    <h3>Helikopterskola</h3>
    <p>Lorem ipsum dolor sit amet, consectetur adipiscing elit, sed do eiusmod</p>
  </div>
  <div class="card" style="left:785px">
    <svg width="64" height="64" viewBox="0 0 64 64" fill="none" stroke="#F7C300" stroke-width="3"><circle cx="32" cy="32" r="28"/><path d="M22 18 V46 M42 18 V46 M22 32 H42"/></svg>
    <h3>Andra Helikopterjobb</h3>
    <p>Lorem ipsum dolor sit amet, consectetur adipiscing elit, sed do eiusmod</p>
  </div>
</section>

<section style="top:820px;height:520px">
  <div class="abs eyebrow" style="left:95px;top:68px">Våra helikoptrar!</div>
  <h2 class="abs heading" style="left:95px;top:102px;font-size:32px">AEROLUX A4</h2>
  <p class="abs body" style="left:95px;top:143px;width:232px;font-size:12px;line-height:1.75">Aerolux A4 är en av världens mest använda helikoptrar. Dels för den är kostnadseffektiv men också väldigt driftsäker. Det finns med flytanordningar och utan. Vi har båda typerna.</p>
  <div class="btn btn-yellow" style="left:95px;top:285px;width:91px;height:33px">Läs mer</div>
  <div class="btn btn-outline" style="left:205px;top:285px;width:90px;height:33px">Boka Nu</div>
  <div class="photo" style="left:353px;top:20px;width:614px;height:370px;background:radial-gradient(ellipse at 50% 60%,#2f6fd0 0%,#1c4fae 30%,#dfe6f0 58%,#fff 75%)" role="img" aria-label="Blå helikopter sedd från sidan"></div>
  <div class="stat" style="top:58px"><i class="dot"></i><div><b>195<small>km/h</small></b><span>Hastighet</span></div></div>
  <div class="stat" style="top:136px"><i class="dot"></i><div><b>3+1</b><span>Passagerare</span></div></div>
  <div class="stat" style="top:218px"><i class="dot"></i><div><b>2,8 <small>Timmar</small></b><span>Räckvidd</span></div></div>
  <div class="stat" style="top:298px"><i class="dot"></i><div><b>4.300<small>m</small></b><span>Begränsningshöjd</span></div></div>
  <div class="abs" style="left:301px;top:442px;width:597px;height:2px;background:#e6e6e6"></div>
  <div class="abs" style="left:301px;top:441px;width:192px;height:4px;background:var(--yellow)"></div>
  <div class="abs" style="left:848px;top:437px;width:50px;height:12px;border-radius:6px;background:var(--blue)"></div>
  <div class="abs" style="left:945px;top:398px;width:164px;height:97px;background:var(--white);box-shadow:0 4px 14px rgba(0,0,0,.14)">
    <div class="photo" style="left:22px;top:14px;width:120px;height:68px;background:radial-gradient(ellipse,#2a63c4 0%,#e8eef6 65%,#fff 80%)" role="img" aria-label="Miniatyr av helikoptern"></div>
  </div>
</section>

<section class="video">
  <div class="photo" style="inset:0;background:linear-gradient(180deg,#4b7fb8 0%,#6f95b8 30%,#3d6fa3 55%,#1c56a0 100%)" role="img" aria-label="Flygbild över Stockholm vid vattnet"></div>
  <h2 class="abs" style="left:0;width:1200px;top:116px;text-align:center;color:var(--white);font-size:31px;font-weight:600;line-height:1.25">Se en fantastisk dag med<br>underhållning i luften med<br>oss</h2>
  <p class="abs" style="left:0;width:1200px;top:246px;text-align:center;color:var(--white);font-size:13px;line-height:1.6">Lorem ipsum dolor sit amet, consectetur adipiscing elit, sed do<br>eiusmod tempor incididunt ut labore</p>
  <svg class="abs" style="left:562px;top:308px" width="76" height="76" viewBox="0 0 76 76"><circle cx="38" cy="38" r="36" fill="rgba(255,255,255,.25)" stroke="#fff" stroke-width="2"/><path d="M30 24 L54 38 L30 52 Z" fill="#fff"/></svg>
</section>

<section class="about">
  <div class="photo" style="left:112px;top:93px;width:480px;height:415px;background:linear-gradient(180deg,#3d8fe0 0%,#7cb6ec 45%,#5c7c3e 70%,#8a5a3a 100%)" role="img" aria-label="Blå helikopter på en landningsplatta"></div>
  <div class="abs eyebrow" style="left:633px;top:120px">Vilka vi är</div>
  <h2 class="abs heading" style="left:633px;top:155px;font-size:31px">Skyvane Sweden AB.<br>Det lilla företaget med<br>de stora möjligheterna</h2>
  <p class="abs body" style="left:633px;top:280px;width:430px;font-size:12px;line-height:1.8">Skyvane startades med visionen att göra helikopterflygning mer tillgänglig i södra Sverige. Att flyga helikopter i sverige är oftast ganska kostsamt och svårt med tillgänglighet. Detta medför att många som har certifikat ofta får vänta länge mellan sina flygningar. Vi vill förbättra tillgängligheten och servicen framförallt med helikopterhyra i skåne och i södra Sverige.</p>
  <div class="btn btn-yellow" style="left:633px;top:465px;width:125px;height:33px">Upptäck mer</div>
</section>

<section style="top:2478px;height:484px">
  <div class="abs eyebrow" style="left:154px;top:144px">Möt vårt team</div>
  <h2 class="abs heading" style="left:154px;top:178px;font-size:32px">träffa vårt<br>expertteam</h2>
  <p class="abs body" style="left:154px;top:264px;width:430px;font-size:12px">Vi är några piloter som fullkomligt älskar att flyga helikopter och önskar att fler ska få kunna flyga helikopter!</p>
  <div class="abs" style="left:154px;top:332px;width:155px;height:3px;background:var(--blue-mist)"></div>
  <div class="abs" style="left:154px;top:332px;width:50px;height:3px;background:var(--yellow)"></div>
  <div class="photo" style="left:612px;top:95px;width:220px;height:292px;background:linear-gradient(180deg,#c9ccd0,#e9eaec 55%,#b9bcc0)" role="img" aria-label="Pilot i vit uniformsskjorta"></div>
  <div class="photo" style="left:847px;top:95px;width:219px;height:292px;background:linear-gradient(180deg,#6f7478,#3a3f47 55%,#2a2e36)" role="img" aria-label="Pilot i mörk flygoverall"></div>
</section>

<section style="top:2962px;height:573px">
  <div class="photo" style="inset:0;background:linear-gradient(160deg,#6e7a3a 0%,#3b5a3c 40%,#1d3c72 70%,#34552f 100%)" role="img" aria-label="Flygbild över skog och sjö"></div>
  <div class="abs" style="left:112px;top:169px;width:487px;height:404px;background:var(--white)">
    <div class="abs eyebrow" style="left:42px;top:44px">Hur det fungerar</div>
    <h2 class="abs heading" style="left:42px;top:76px;font-size:31px">Vill du hyra helikopter av<br>oss?</h2>
    <p class="abs how-text" style="left:42px;top:164px;width:420px">Ring oss eller skicka ett mail så återkommer vi så snart som möjligt.<br>Skriv ner när du vill hyra, hur mycket du har flugit och vilka dina behörigheter är. Undrar du något annat är du välkommen att skriva med den frågan ideal. Vill du ha hjälp med något annat gällande flygning. Exempelvis invetering från Skyvane i skåne kan du även fråga det här.</p>
    <p class="abs" style="left:42px;top:346px;color:var(--yellow);font-size:12px">info@skyvane-demo.se</p>
  </div>
</section>

<section style="top:3535px;height:766px">
  <div class="photo" style="left:112px;top:93px;width:437px;height:580px;background:linear-gradient(135deg,#2b5ca6 0%,#7aa6d8 40%,#c89a78 60%,#274f8e 100%)" role="img" aria-label="Leende pilot i helikopterns cockpit"></div>
  <div class="abs" style="left:409px;top:134px;width:690px;height:520px;background:var(--white)"></div>
  <div class="abs eyebrow" style="left:450px;top:196px">Vittnesmål</div>
  <h2 class="abs heading" style="left:450px;top:234px;font-size:31px">Vad de sager.</h2>
  <p class="abs body" style="left:450px;top:282px;font-size:12px">Lorem ipsum dolor sit amet, consectetur adipiscing</p>
  <div class="abs" style="left:456px;top:321px;width:155px;height:3px;background:var(--blue-mist)"></div>
  <div class="abs" style="left:456px;top:321px;width:50px;height:3px;background:var(--yellow)"></div>
</section>
<div class="quote" style="left:456px;width:247px">
  <p>"Lorem ipsum dolor sit amet, consectetur adipiscing elit, sed do eiusmod tempor incididunt ut labore et dolore magna aliqua. Ut enim ad minim veniam"</p>
  <div class="author"><i role="img" aria-label="Kundporträtt"></i><div><b>Erik Lindqvist</b><span>From Malmö</span></div></div>
</div>
<div class="quote" style="left:791px;width:297px">
  <p>"Lorem ipsum dolor sit amet, consectetur adipiscing elit, sed do eiusmod tempor incididunt ut labore et dolore magna aliqua. Ut enim ad minim veniam"</p>
  <div class="author"><i role="img" aria-label="Kundporträtt"></i><div><b>Erik Lindqvist</b><span>From Malmö</span></div></div>
</div>

<section class="partners">
  <div class="partner"><i style="border-radius:50%"></i>Nordwing</div>
  <div class="partner"><i></i>Aerova</div>
  <div class="partner"><i style="border-radius:50%"></i>Skylark</div>
  <div class="partner">Fjordair<i style="border-radius:50%"></i></div>
</section>

<footer class="footer">
  <div class="brand" style="left:112px;top:68px"><i></i>SKYVANE</div>
  <p style="left:112px;top:112px;width:220px">Lorem ipsum dolor sit amet, consectetur adipiscing elit, sed do eiusmod tempor</p>
  <h4 style="left:404px">Öppetider</h4>
  <p style="left:404px;top:110px">Måndag – Söndag:<br><br>09.00 – 17.00<br>Övrig tid enligt<br>överenskommelse.</p>
  <h4 style="left:623px">Kontakt</h4>
  <p style="left:623px;top:110px">Skyvane,<br>Norrvik Flygfält,<br><br>+46 (0) 700 123 456<br>info@skyvane-demo.se</p>
  <h4 style="left:846px">Nyhetsbrev</h4>
  <p style="left:846px;top:110px;width:250px">Anmäl dig till vårt nyhetsbrev för att få uppdaterad information, insikt eller marknadsföring.</p>
  <div class="abs" style="left:846px;top:171px;width:242px;height:35px;background:var(--white);color:var(--blue-mid);font-size:12px;padding:10px 14px">Email</div>
  <div class="btn btn-yellow" style="left:846px;top:213px;width:242px;height:34px">Sign Up</div>
  <p style="left:0;width:1200px;top:300px;text-align:center">Copyright © 2022 Skyvane. All rights reserved.</p>
</footer>

</body>
</html>
```